Business Card for Pet Food Deliver

Looking for a business card design for a start up company. We are Brisk Hound, Premium Pet Products Brought Round.

We market and are designing a website where our clients can go to and order pet food. We then deliver to a local client base. We do person to person deliver, we do not ship at this point. We are starting off with dog and cat food and treats.

Attached is our logo. We are looking for a fun yet professional design. Eye catching with color but not over the top with color. Looking for a double sided card. Contact info on the front and our logo on the back maybe. . .

I am a huge green fan. However, I am thinking I like the orange a bit more then the blue and green for dominant colors. . .

I am attaching our logo.

The file that has our slogan under has a minor change not implemented yet. The word 'Premium' should be gray to match and the word 'Delivered' should be black to match.

Target Market(s)

We are looking to service those pet owners looking for the convenience of not having to drive to a pet store to purchase their products. We are looking for those who are web savvy and purchase online.

We will also be targeting seniors in senior communities without consistent transprotation.

Industry/Entity Type

Pet

Font styles to use
Sans Serif

Colors
f37122
3176b5
acd036

Requirements
Must have
• Double sided. Logo only on one side with a bold color for the background.

Space for name, phone number, website address, mailing address.
Should not have
• No paws, delivery trucks.

```html
<!DOCTYPE html>
<html lang="en">
<head>
<meta charset="utf-8">
<title>Brisk Hound – Business Card</title>
<link rel="stylesheet" href="https://fonts.googleapis.com/css2?family=Source+Sans+3:ital,wght@0,400;0,600;1,400;1,700&family=PT+Serif:wght@400;700&display=swap">
<style>
  :root {
    --green: #acd036;
    --blue: #3176b5;
    --orange: #f37122;
    --white: #ffffff;
    --ink: #5a5a5a;
    --ink-soft: #6e6e6e;
    --backdrop: #ececec;
  }
  * { margin: 0; padding: 0; box-sizing: border-box; }
  html, body {
    width: 1200px; height: 1200px; overflow: hidden;
    background: var(--backdrop);
  }
  .sheet {
    width: 1200px; height: 1200px;
    display: flex; flex-direction: column; align-items: center; justify-content: center;
    gap: 60px;
  }
  .card {
    position: relative;
    width: 880px; height: 503px;
    overflow: hidden;
    box-shadow: 0 6px 18px rgba(0,0,0,0.18);
  }

  /* Logo side */
  .card--brand { background: var(--green); }
  .brand-disc {
    position: absolute; left: 50%; top: 50%;
    width: 420px; height: 420px; margin: -210px 0 0 -210px;
    border-radius: 50%; background: var(--white);
    display: flex; flex-direction: column; align-items: center; justify-content: center;
    text-align: center;
  }
  .brand-name {
    font-family: "Source Sans 3", sans-serif;
    font-weight: 400; font-size: 58px; letter-spacing: 0.5px;
    color: var(--ink);
    line-height: 1;
  }
  .brand-tagline {
    margin-top: 14px;
    font-family: "Source Sans 3", sans-serif;
    font-weight: 400; font-size: 17px; letter-spacing: 1.5px;
    text-transform: uppercase;
    color: var(--ink-soft);
  }

  /* Contact side */
  .card--contact { background: var(--green); }
  .contact-field { position: absolute; inset: 0; width: 880px; height: 503px; }
  .person { position: absolute; left: 250px; top: 70px; }
  .person-name {
    font-family: "Source Sans 3", sans-serif;
    font-weight: 700; font-style: italic; font-size: 34px;
    color: var(--ink);
  }
  .person-role {
    font-family: "Source Sans 3", sans-serif;
    font-style: italic; font-size: 26px;
    color: var(--ink);
    margin-top: -4px;
  }
  .contact-icons { position: absolute; left: 0; top: 150px; }
  .contact-icons svg { display: block; margin-bottom: 8px; }
  .contact-lines {
    position: absolute; left: 130px; top: 205px;
    font-family: "PT Serif", serif; font-size: 25px; line-height: 1.25;
    color: var(--ink);
  }
  .contact-lines .phone { margin-bottom: 6px; }
  .website {
    position: absolute; right: 40px; bottom: 42px;
    font-family: "PT Serif", serif; font-weight: 700; font-size: 27px;
    color: var(--white);
  }
</style>
</head>
<body>
<main class="sheet">

  <section class="card card--brand" aria-label="Card back with brand name">
    <div class="brand-disc">
      <p class="brand-name">Brisk Hound</p>
      <p class="brand-tagline">Premium Pet Products Brought Round</p>
    </div>
  </section>

  <section class="card card--contact" aria-label="Card front with contact details">
    <svg class="contact-field" viewBox="0 0 880 503" aria-hidden="true">
      <path d="M0 0 H880 V170 C760 300 520 360 330 350 C200 343 80 320 0 290 Z" fill="#ffffff"/>
    </svg>

    <div class="person">
      <p class="person-name">Daniel Ashworth</p>
      <p class="person-role">Nutrition Specialist</p>
    </div>

    <div class="contact-icons">
      <svg width="110" height="44" viewBox="0 0 110 44" aria-label="Phone">
        <rect width="110" height="44" fill="var(--blue)"/>
        <path d="M76 12 c-2 0 -4 2 -4 4 c0 9 7 16 16 16 c2 0 4 -2 4 -4 l-1 -3 l-5 -1 l-2 2 c-3 -1 -6 -4 -7 -7 l2 -2 l-1 -5 z" fill="#ffffff"/>
      </svg>
      <svg width="110" height="44" viewBox="0 0 110 44" aria-label="Location">
        <rect width="110" height="44" fill="var(--orange)"/>
        <path d="M84 8 a9 9 0 0 1 9 9 c0 7 -9 18 -9 18 s-9 -11 -9 -18 a9 9 0 0 1 9 -9 z" fill="#ffffff"/>
        <circle cx="84" cy="17" r="3.5" fill="var(--orange)"/>
      </svg>
    </div>

    <div class="contact-lines">
      <p class="phone">555-214-0386</p>
      <p>742 Alder Lane</p>
      <p>Millbrook, WI 5410</p>
    </div>

    <p class="website">www.briskhounddelivers.com</p>
  </section>

</main>
</body>
</html>
```